Villa Sereno needs a new website for its boutique apartment

We are a boutique apartment in Florence that rents out to tourists. We are looking to redesign our website. See the existing site at www.villaserenostay.example

Ideally redesigned site would enable us to easily add and change photos in the gallery and across the site.

The new logo for the apartment is currently under design but being based around the current house logo with a person standing inside.
Updates

Project Deadline Extended
Reason: The website design by the 1st Place designer has been long and drawn out and not led to the design that we were looking for. As such, we are extending the deadline for another 5 days to hopefully get new designs and options.

Target Market(s)

Global tourists

Industry/Entity Type

Accommodation

Coding

Coded - Design and coding required

Number of Pages Required

5+ page

Font styles to use
Sans Serif

Requirements
Must have
• Welcome page, gallery page, information page about apartment and availability page with link to booking sites. And option for another page with tourist information. We must be able to change the photos in the gallery with relative ease when required.
• The Villa Sereno font has been uploaded which is used with the logo and the new logo has been uploaded.
Nice to have
• Looking like a fun but professional hotel site
• Page info is located on www.villaserenostay.example site

```html
<!DOCTYPE html>
<html lang="en">
<head>
<meta charset="utf-8">
<title>Villa Sereno – Holiday Apartments in Florence</title>
<link href="https://fonts.googleapis.com/css2?family=Raleway:wght@300;400;500;700&family=Open+Sans:wght@400;600&display=swap" rel="stylesheet">
<style>
  :root {
    --ink: #1e1e1e;
    --text: #3b3b3b;
    --muted: #6a6a6a;
    --white: #ffffff;
    --black: #000000;
    --band-light: #f2f2f2;
    --footer: #3a3a3a;
    --footer-line: #8a8a8a;
    --nav-glass: rgba(255, 255, 255, 0.72);
    --gallery-shade: rgba(20, 18, 16, 0.55);
  }
  * { box-sizing: border-box; margin: 0; padding: 0; }
  html, body { width: 1200px; height: 3103px; overflow: hidden; }
  body { position: relative; background: var(--white); font-family: "Raleway", sans-serif; color: var(--text); }
  .abs { position: absolute; }

  /* Hero */
  .hero { position: absolute; left: 0; top: 0; width: 1200px; height: 710px; }
  .hero-photo { position: absolute; inset: 0;
    background: linear-gradient(180deg, #8f8679 0%, #b9ad9c 30%, #9a8b78 55%, #4a3d33 80%, #2a221d 100%); }
  .topnav { position: absolute; left: 0; top: 0; width: 1200px; height: 62px; background: var(--nav-glass); }
  .topnav .tagline { position: absolute; left: 79px; top: 20px; font-weight: 700; font-size: 17px; color: var(--ink); }
  .topnav a { position: absolute; top: 20px; font-size: 19px; color: var(--ink); text-decoration: none; transform: translateX(-50%); white-space: nowrap; }
  .logo-diamond { position: absolute; left: 466px; top: 202px; width: 362px; height: 362px; }
  .logo-name { position: absolute; left: 467px; top: 400px; width: 360px; text-align: center; font-size: 34px; font-weight: 400; color: var(--ink); }

  /* Search */
  .search-bar { position: absolute; left: 0; top: 710px; width: 1200px; height: 89px; background: var(--black); }
  .search-bar label { position: absolute; top: 17px; font-family: "Open Sans", sans-serif; font-size: 12px; color: var(--white); }
  .field { position: absolute; top: 39px; height: 31px; background: var(--white); font-family: "Open Sans", sans-serif; font-size: 14px; color: var(--ink); padding: 6px 8px; }
  .field svg { position: absolute; right: 7px; top: 7px; }
  .stepper { position: absolute; right: 0; top: 0; width: 28px; height: 31px; border-left: 1px solid #999; }
  .search-btn { position: absolute; left: 943px; top: 39px; width: 104px; height: 31px; background: var(--white); text-align: center; font-size: 17px; line-height: 31px; color: var(--ink); }

  /* Welcome */
  .section-title { position: absolute; left: 0; width: 1200px; text-align: center; font-weight: 400; font-size: 45px; color: var(--ink); }
  .welcome-text { position: absolute; left: 150px; top: 938px; width: 900px; text-align: center; font-family: "Open Sans", sans-serif; font-size: 15.5px; line-height: 33px; color: var(--text); }

  /* Gallery */
  .gallery { position: absolute; left: 0; top: 1138px; width: 1200px; height: 730px; }
  .gallery-bg { position: absolute; inset: 0; background: linear-gradient(160deg, #2c3b3a 0%, #4b4a44 45%, #2f2a25 100%); }
  .gallery-bg::after { content: ""; position: absolute; inset: 0; background: var(--gallery-shade); }
  .gallery .section-title { color: var(--white); top: 72px; }
  .thumb { position: absolute; width: 336px; height: 210px; border: 3px solid var(--white); }
  .thumb-hover { position: absolute; inset: 0; background: rgba(255,255,255,0.35); display: flex; align-items: center; justify-content: center; }
  .outline-btn { position: absolute; border: 2px solid currentColor; text-align: center; font-size: 18px; }
  .view-all { left: 528px; top: 652px; width: 144px; height: 43px; line-height: 39px; color: var(--white); border-color: rgba(255,255,255,0.8); }

  /* Why book */
  .why { position: absolute; left: 0; top: 1868px; width: 1200px; height: 573px; background: var(--band-light); }
  .why h2 { position: absolute; left: 101px; top: 40px; font-weight: 400; font-size: 45px; color: var(--ink); }
  .perks { position: absolute; left: 97px; top: 127px; list-style: none; }
  .perks li { display: flex; align-items: center; height: 31px; font-family: "Open Sans", sans-serif; font-size: 15px; color: var(--ink); }
  .perks svg { margin-right: 14px; }
  .check-btn { left: 101px; top: 298px; width: 220px; height: 42px; line-height: 38px; font-size: 17px; color: var(--ink); }
  .map { position: absolute; left: 685px; top: 46px; width: 418px; height: 296px; border: 2px solid var(--ink);
    background: linear-gradient(135deg, #e9e4d8 0%, #f1ece0 45%, #dfe6d4 70%, #e8e3d5 100%); }
  .why hr { position: absolute; left: 77px; top: 391px; width: 1046px; border: 0; border-top: 1px solid #d4d4d4; }
  .amenity { position: absolute; top: 432px; width: 200px; text-align: center; transform: translateX(-50%); }
  .amenity svg { display: block; margin: 0 auto 10px; }
  .amenity span { font-family: "Open Sans", sans-serif; font-size: 15px; color: var(--ink); }

  /* Testimonials */
  .reviews .section-title { top: 2490px; }
  .quote-mark { position: absolute; }
  .review-text { position: absolute; left: 228px; top: 2570px; width: 744px; text-align: center; font-family: "Open Sans", sans-serif; font-size: 13px; line-height: 22px; color: var(--muted); }
  .reviewer { position: absolute; left: 0; top: 2651px; width: 1200px; text-align: center; font-size: 21px; color: var(--ink); }
  .avatar { position: absolute; left: 555px; top: 2695px; width: 86px; height: 86px; border-radius: 50%; border: 3px solid var(--footer);
    background: radial-gradient(circle at 50% 40%, #d9c9b8 0%, #a99a8c 60%, #6d645c 100%); }

  /* Footer */
  .footer { position: absolute; left: 0; top: 2830px; width: 1200px; height: 211px; background: var(--footer); }
  .footer-nav a { position: absolute; top: 32px; font-size: 18px; color: var(--white); text-decoration: none; }
  .social { position: absolute; top: 23px; width: 38px; height: 38px; border-radius: 50%; background: var(--white); }
  .footer hr { position: absolute; left: 77px; top: 93px; width: 1046px; border: 0; border-top: 1px solid var(--footer-line); }
  .contact { position: absolute; top: 124px; display: flex; align-items: center; font-family: "Open Sans", sans-serif; font-size: 14px; color: var(--white); line-height: 20px; }
  .contact .badge { width: 30px; height: 30px; border-radius: 50%; background: var(--white); display: flex; align-items: center; justify-content: center; margin-right: 18px; flex: none; }
  .copyright { position: absolute; left: 0; top: 3041px; width: 1200px; height: 62px; background: var(--black); color: var(--white); text-align: center; line-height: 62px; font-family: "Open Sans", sans-serif; font-size: 15px; }
  .copyright b { font-weight: 600; }
</style>
</head>
<body>

<header class="hero">
  <div class="hero-photo" role="img" aria-label="Photo of the apartment living room with sofa, red bean bag and wooden dining table"></div>
  <nav class="topnav">
    <span class="tagline">Holiday Apartments in Florence</span>
    <a href="#" style="left:478px">HOME</a>
    <a href="#" style="left:602px">ABOUT US</a>
    <a href="#" style="left:739px">GALLERY</a>
    <a href="#" style="left:888px">CONTECT US</a>
    <a href="#" style="left:1055px">AVAILABILITY</a>
  </nav>
  <svg class="logo-diamond" viewBox="0 0 362 362" aria-hidden="true">
    <polygon points="181,0 362,181 181,362 0,181" fill="rgba(255,255,255,0.78)"/>
  </svg>
  <div class="logo-name">Villa Sereno</div>
</header>

<form class="search-bar">
  <label style="left:153px">Check In</label>
  <div class="field" style="left:153px;width:228px">DD MM YYYY
    <svg width="18" height="17" viewBox="0 0 18 17"><rect x="1" y="2" width="16" height="14" fill="none" stroke="#333" stroke-width="1.5"/><rect x="1" y="2" width="16" height="4" fill="#333"/><path d="M4 9h2M8 9h2M12 9h2M4 12h2M8 12h2M12 12h2" stroke="#333" stroke-width="1.5"/></svg>
  </div>
  <label style="left:424px">Check Out</label>
  <div class="field" style="left:424px;width:226px">DD MM YYYY
    <svg width="18" height="17" viewBox="0 0 18 17"><rect x="1" y="2" width="16" height="14" fill="none" stroke="#333" stroke-width="1.5"/><rect x="1" y="2" width="16" height="4" fill="#333"/><path d="M4 9h2M8 9h2M12 9h2M4 12h2M8 12h2M12 12h2" stroke="#333" stroke-width="1.5"/></svg>
  </div>
  <label style="left:693px">Adults</label>
  <div class="field" style="left:693px;width:93px;padding-left:22px">1
    <span class="stepper"><svg width="28" height="31" viewBox="0 0 28 31" style="right:0;top:0"><path d="M9 12l5-5 5 5M9 19l5 5 5-5" fill="none" stroke="#333" stroke-width="1.8"/></svg></span>
  </div>
  <label style="left:817px">Kids</label>
  <div class="field" style="left:817px;width:93px;padding-left:22px">1
    <span class="stepper"><svg width="28" height="31" viewBox="0 0 28 31" style="right:0;top:0"><path d="M9 12l5-5 5 5M9 19l5 5 5-5" fill="none" stroke="#333" stroke-width="1.8"/></svg></span>
  </div>
  <div class="search-btn">SEARCH</div>
</form>

<section class="welcome">
  <h1 class="section-title" style="top:846px">Welcome to Villa Sereno</h1>
  <p class="welcome-text">"Villa Sereno" is a newly renovated boutique 2-bedroom loft apartment in the historic centre of Florence (Firenze), Italy. "Villa Sereno" is perfectly located for your Tuscan holiday, offering easy walking access to all of central Florence - only 600m from the Duomo and Ponte Vecchio. The apartment is configured to sleep up to six and is furnished with elegant and luxury fittings, and has complimentary high-speed internet and cable-TV.</p>
</section>

<section class="gallery">
  <div class="gallery-bg" role="img" aria-label="Dimmed background photo of bathroom toiletries"></div>
  <h2 class="section-title">Our Gallery</h2>
  <div class="thumb" style="left:77px;top:143px;background:linear-gradient(135deg,#e7e3dc,#c9b9a3 60%,#9b3a2c)" role="img" aria-label="Living area with stairs, red bean bag and dining table"></div>
  <div class="thumb" style="left:432px;top:143px;background:linear-gradient(135deg,#6d6a66,#d6d3cf 60%,#a39d95)" role="img" aria-label="Bedroom with white bed">
    <div class="thumb-hover"><svg width="34" height="34" viewBox="0 0 34 34"><circle cx="14" cy="14" r="10" fill="none" stroke="#fff" stroke-width="4"/><path d="M21 21l10 10" stroke="#fff" stroke-width="5" stroke-linecap="round"/></svg></div>
  </div>
  <div class="thumb" style="left:788px;top:143px;background:linear-gradient(135deg,#efece8,#cfc8bd 55%,#5c4a3c)" role="img" aria-label="White kitchen with dining table and flowers"></div>
  <div class="thumb" style="left:77px;top:393px;background:linear-gradient(135deg,#b7a68c,#e8e4de 55%,#8a6a4f)" role="img" aria-label="Bedroom with armchair and bed"></div>
  <div class="thumb" style="left:432px;top:393px;background:linear-gradient(135deg,#5b5147,#a08a6f 55%,#3d342d)" role="img" aria-label="Loft workspace with lamp and wooden beams"></div>
  <div class="thumb" style="left:788px;top:393px;background:linear-gradient(135deg,#d8d4cd,#8a8f98 55%,#3a4a6a)" role="img" aria-label="Bedroom with blue bedding and window"></div>
  <div class="outline-btn view-all">VIEW ALL</div>
</section>

<section class="why">
  <h2>Why book with us</h2>
  <ul class="perks">
    <li><svg width="16" height="14" viewBox="0 0 16 14"><path d="M8 1L1 7h2v6h4V9h2v4h4V7h2z" fill="#1e1e1e"/></svg>Nearest Airport 8 Kilometres Florence Airport (FLR)</li>
    <li><svg width="16" height="14" viewBox="0 0 16 14"><path d="M8 1L1 7h2v6h4V9h2v4h4V7h2z" fill="#1e1e1e"/></svg>Nearest Beach 100 Kilometres Via Reggio</li>
    <li><svg width="16" height="14" viewBox="0 0 16 14"><path d="M8 1L1 7h2v6h4V9h2v4h4V7h2z" fill="#1e1e1e"/></svg>Nearest Train 600 Metres Santa Maria Novella</li>
    <li><svg width="16" height="14" viewBox="0 0 16 14"><path d="M8 1L1 7h2v6h4V9h2v4h4V7h2z" fill="#1e1e1e"/></svg>Private parking in the same building</li>
    <li><svg width="16" height="14" viewBox="0 0 16 14"><path d="M8 1L1 7h2v6h4V9h2v4h4V7h2z" fill="#1e1e1e"/></svg>Solarium and terrace on the roof</li>
  </ul>
  <div class="outline-btn check-btn">CHECK AVAILABILITY</div>
  <div class="map" role="img" aria-label="Street map of central Florence showing the apartment location"></div>
  <hr>
  <div class="amenity" style="left:182px">
    <svg width="40" height="36" viewBox="0 0 40 36"><path d="M4 13a23 23 0 0 1 32 0M9 19a15 15 0 0 1 22 0M14 25a8 8 0 0 1 12 0" fill="none" stroke="#333" stroke-width="2"/><circle cx="20" cy="31" r="2.5" fill="#333"/></svg>
    <span>Free WiFi</span>
  </div>
  <div class="amenity" style="left:391px">
    <svg width="40" height="36" viewBox="0 0 40 36"><path d="M11 3h18l-3 13H14z" fill="none" stroke="#333" stroke-width="2"/><path d="M20 16v16M13 33h14" stroke="#333" stroke-width="2"/></svg>
    <span>Fully Furnished</span>
  </div>
  <div class="amenity" style="left:600px">
    <svg width="40" height="36" viewBox="0 0 40 36"><circle cx="20" cy="18" r="15" fill="none" stroke="#333" stroke-width="2"/><path d="M16 26V10h6a4.5 4.5 0 0 1 0 9h-6" fill="none" stroke="#333" stroke-width="2"/></svg>
    <span>Free Parking</span>
  </div>
  <div class="amenity" style="left:809px">
    <svg width="40" height="36" viewBox="0 0 40 36"><path d="M34 3c-2-1-5 1-8 4L21 12 7 8 4 11l11 7-6 6-5-1-2 2 6 4 4 6 2-2-1-5 6-6 7 11 3-3-4-14 5-5c3-3 5-6 4-8z" fill="none" stroke="#333" stroke-width="1.8" stroke-linejoin="round"/></svg>
    <span>Airport Transfers</span>
  </div>
  <div class="amenity" style="left:1018px">
    <svg width="40" height="36" viewBox="0 0 40 36"><path d="M33 2L20 20" stroke="#333" stroke-width="2"/><path d="M17 18l6 5-8 11-9-8z" fill="none" stroke="#333" stroke-width="2" stroke-linejoin="round"/><path d="M9 28l5-6M12 31l5-6" stroke="#333" stroke-width="1.5"/></svg>
    <span>Cleaning Services</span>
  </div>
</section>

<section class="reviews">
  <h2 class="section-title">What tourists say</h2>
  <svg class="quote-mark" style="left:152px;top:2548px" width="56" height="44" viewBox="0 0 56 44"><path d="M2 42V24C2 10 9 3 22 1l2 6c-8 2-11 7-11 13h10v22zM32 42V24c0-14 7-21 20-23l2 6c-8 2-11 7-11 13h10v22z" fill="#8a8a8a"/></svg>
  <p class="review-text">The location is perfect in the historic center, closed to everything. The apartment is just renovated and was perfect for our family of four(you can stay up to 6 I think). There was tons of really good restaurants outside on the street and also walking distance to the main train station(sm novella)</p>
  <svg class="quote-mark" style="left:984px;top:2610px" width="56" height="44" viewBox="0 0 56 44"><path d="M54 2v18c0 14-7 21-20 23l-2-6c8-2 11-7 11-13H33V2zM24 2v18c0 14-7 21-20 23l-2-6c8-2 11-7 11-13H3V2z" fill="#8a8a8a"/></svg>
  <div class="reviewer">Marco Bellini</div>
  <div class="avatar" role="img" aria-label="Portrait photo of the guest"></div>
</section>

<footer class="footer">
  <nav class="footer-nav">
    <a href="#" style="left:79px">HOME</a>
    <a href="#" style="left:184px">ABOUT US</a>
    <a href="#" style="left:326px">GALLERY</a>
    <a href="#" style="left:458px">CONTECT US</a>
    <a href="#" style="left:625px">AVAILABILITY</a>
  </nav>
  <span class="social" style="left:924px" aria-label="Listing site"></span>
  <span class="social" style="left:976px" aria-label="Listing site"></span>
  <span class="social" style="left:1028px" aria-label="Review site"></span>
  <span class="social" style="left:1080px" aria-label="Booking site"></span>
  <hr>
  <div class="contact" style="left:84px">
    <span class="badge"><svg width="14" height="18" viewBox="0 0 14 18"><path d="M7 1a6 6 0 0 0-6 6c0 5 6 10 6 10s6-5 6-10a6 6 0 0 0-6-6z" fill="#3a3a3a"/><circle cx="7" cy="7" r="2.2" fill="#fff"/></svg></span>
    <span>Lorem Ipsum is simply dummy text<br>of the printing.</span>
  </div>
  <div class="contact" style="left:510px">
    <span class="badge"><svg width="16" height="16" viewBox="0 0 16 16"><path d="M3 1l3 3-1.5 2.5a9 9 0 0 0 5 5L12 10l3 3-2 2C7 15 1 9 1 3z" fill="#3a3a3a"/></svg></span>
    <span>39 342 555 0187</span>
  </div>
  <div class="contact" style="left:827px">
    <span class="badge"><svg width="16" height="12" viewBox="0 0 16 12"><rect x="1" y="1" width="14" height="10" fill="none" stroke="#3a3a3a" stroke-width="1.6"/><path d="M1 1l7 6 7-6" fill="none" stroke="#3a3a3a" stroke-width="1.6"/></svg></span>
    <span>reservations@villaserenostay.example</span>
  </div>
</footer>

<div class="copyright">© <b>VillaSereno</b> - 2016. All Rights Reserved.</div>

</body>
</html>
```